Business cards - KESTO Roofing & Siding

We need simple business cards made up for our Roofing & Siding business based in Calgary Alberta.
The logo on one side of the card and potentially our slogan "Built with trust, verified by time".
The other side could have:
-A small logo
-Rep name:
-Rep cell phone:
-Rep email:
-Office phone: 403-386-2049
-Website: PrairieShinglePros.com

We would like to incorporate the colours from our logo, especially the lite blue on the jpeg file. I have attached the ai file and jpeg file. We like the colours better on the jpeg file.

I do not require a money back guarantee

```html
<!DOCTYPE html>
<html lang="en">
<head>
<meta charset="utf-8">
<title>KESTO Roofing &amp; Siding – Business Cards</title>
<link href="https://fonts.googleapis.com/css2?family=Montserrat:wght@400;500;600&display=swap" rel="stylesheet">
<style>
  :root {
    --page-bg: #141414;
    --card-bg: #1f1f1f;
    --brand-blue: #1e8fef;
    --text-white: #f4f4f4;
  }
  * { margin: 0; padding: 0; box-sizing: border-box; }
  html, body { width: 1200px; height: 900px; overflow: hidden; }
  body {
    background: var(--page-bg);
    font-family: "Montserrat", sans-serif;
    color: var(--text-white);
    display: flex;
    flex-direction: column;
    align-items: center;
    justify-content: center;
    gap: 40px;
  }
  .card {
    width: 680px;
    height: 388px;
    background: var(--card-bg);
    border-radius: 4px;
    position: relative;
  }
  .card--front {
    display: flex;
    align-items: center;
    justify-content: center;
  }
  .wordmark {
    display: flex;
    align-items: center;
    gap: 14px;
  }
  .wordmark__mark {
    width: 22px;
    height: 22px;
    background: var(--brand-blue);
  }
  .wordmark__name {
    font-weight: 600;
    color: var(--text-white);
    letter-spacing: 0.08em;
    text-transform: uppercase;
    line-height: 1.15;
  }
  .card--front .wordmark__name { font-size: 30px; }
  .card--back {
    display: flex;
    align-items: center;
    padding: 0 48px;
  }
  .card--back .wordmark { width: 290px; }
  .card--back .wordmark__name { font-size: 22px; }
  .divider {
    width: 2px;
    height: 150px;
    background: var(--brand-blue);
    margin: 0 34px 0 14px;
  }
  .rep__name {
    font-size: 30px;
    font-weight: 600;
    color: var(--brand-blue);
    text-transform: uppercase;
    line-height: 1;
  }
  .rep__title {
    font-size: 18px;
    font-weight: 500;
    text-transform: uppercase;
    margin: 4px 0 12px;
  }
  .contact-list { list-style: none; }
  .contact-list li {
    display: flex;
    align-items: center;
    gap: 10px;
    font-size: 19px;
    line-height: 1.35;
  }
  .contact-list svg { width: 13px; height: 13px; flex: none; }
</style>
</head>
<body>
  <section class="card card--front">
    <div class="wordmark">
      <span class="wordmark__mark"></span>
      <span class="wordmark__name">KESTO Roofing &amp; Siding</span>
    </div>
  </section>

  <section class="card card--back">
    <div class="wordmark">
      <span class="wordmark__mark"></span>
      <span class="wordmark__name">KESTO Roofing<br>&amp; Siding</span>
    </div>
    <div class="divider"></div>
    <div class="rep">
      <h1 class="rep__name">Daniel Marsh</h1>
      <p class="rep__title">Director</p>
      <ul class="contact-list">
        <li>
          <svg viewBox="0 0 16 16" aria-hidden="true"><path d="M3 1l3 3-1.5 2a9 9 0 0 0 5.5 5.5L12 10l3 3-2 2C7 15 1 9 1 3z" fill="none" stroke="var(--brand-blue)" stroke-width="1.6"/></svg>
          403-386-2049
        </li>
        <li>
          <svg viewBox="0 0 16 16" aria-hidden="true"><rect x="4" y="1" width="8" height="14" rx="1.5" fill="none" stroke="var(--brand-blue)" stroke-width="1.6"/><line x1="7" y1="12.5" x2="9" y2="12.5" stroke="var(--brand-blue)" stroke-width="1.6"/></svg>
          587-214-6630
        </li>
        <li>
          <svg viewBox="0 0 16 16" aria-hidden="true"><rect x="1" y="3" width="14" height="10" rx="1" fill="none" stroke="var(--brand-blue)" stroke-width="1.6"/><path d="M1 3l7 6 7-6" fill="none" stroke="var(--brand-blue)" stroke-width="1.6"/></svg>
          kestoroof@mailbox.ca
        </li>
        <li>
          <svg viewBox="0 0 16 16" aria-hidden="true"><circle cx="8" cy="8" r="6.5" fill="none" stroke="var(--brand-blue)" stroke-width="1.4"/><ellipse cx="8" cy="8" rx="3" ry="6.5" fill="none" stroke="var(--brand-blue)" stroke-width="1.2"/><line x1="1.5" y1="8" x2="14.5" y2="8" stroke="var(--brand-blue)" stroke-width="1.2"/></svg>
          PrairieShinglePros.com
        </li>
      </ul>
    </div>
  </section>
</body>
</html>
```